Flyer Design - Child Care Centre

I need a flyer design (d/sided), full colour for a Child Care Centre that I have recently bought. Check out my website (tiny-sprouts.com.au) for information on what we do, our services, philosophy, fees and hours of operation.

The purpose of this flyer is to advertise our services as a child care centre (under new management) to the local community and with various hospitals.

The flyer should embody our philosophy, the text on my home page (particularly our QX focus) and some of the parent testimonials. It should also include my logo and Zibb (refer attached AI and jpeg files, eps available on request).

Feel free to add stock photo's of kids and cartoon characters and use the following CMYK colours if incorporating any coloured text. Green: C-78, M-0, Y-100, K-0 Magenta: C-0, M-100, Y-33, K-10

```html
<!DOCTYPE html>
<html lang="en">
<head>
<meta charset="utf-8">
<title>Tiny Sprouts – Flyer Back</title>
<link rel="stylesheet" href="https://fonts.googleapis.com/css2?family=Lato:wght@400;700&family=Mountains+of+Christmas:wght@700&display=swap">
<style>
  :root {
    --page-bg: #ecebe8;
    --paper: #fdf6e6;
    --ink: #464646;
    --green: #25b34b;
    --purple: #a13a93;
    --purple-dark: #76246a;
    --white: #ffffff;
    --photo-a: #f3d9b8;
    --photo-b: #dfe6d4;
    --doodle: #c9a6cf;
  }
  * { margin: 0; padding: 0; box-sizing: border-box; }
  html, body { width: 1200px; height: 800px; overflow: hidden; background: var(--page-bg); }
  body { position: relative; font-family: "Lato", sans-serif; }

  .flyer {
    position: absolute; left: 215px; top: 107px; width: 843px; height: 597px;
    background: var(--paper); overflow: hidden;
    box-shadow: 0 6px 24px rgba(0,0,0,.12);
  }

  .kids-photo {
    position: absolute; left: 0; top: 10px; width: 430px; height: 380px;
    background: radial-gradient(ellipse at 50% 55%, var(--photo-a) 0%, #f1e4cf 45%, var(--photo-b) 80%, rgba(253,246,230,0) 100%);
  }
  .cap-doodle, .bulb-doodle {
    position: absolute; border-radius: 50%; background: var(--doodle); opacity: .45;
  }
  .cap-doodle { left: 133px; top: 15px; width: 70px; height: 48px; }
  .bulb-doodle { left: 345px; top: 40px; width: 40px; height: 50px; }

  .contact-panel { position: absolute; left: 0; top: 0; width: 843px; height: 597px; }

  .contact {
    position: absolute; left: 25px; top: 355px; color: var(--white);
  }
  .contact h2 {
    font-family: "Mountains of Christmas", cursive; font-weight: 700;
    font-size: 40px; line-height: 1; margin-left: 22px; margin-bottom: 28px; letter-spacing: .5px;
  }
  .contact p { font-size: 12.5px; line-height: 21px; }
  .social { margin-top: 10px; }
  .social p { display: flex; align-items: center; gap: 5px; line-height: 22px; }
  .social .dot { width: 12px; height: 12px; border-radius: 50%; background: var(--white); opacity: .8; }
  .social strong { font-weight: 700; }

  .reader-girl {
    position: absolute; left: 425px; top: 15px; width: 60px; height: 52px;
    background: #f2d27a; border-radius: 40% 40% 30% 30%; opacity: .8;
  }
  .testimonials-title {
    position: absolute; left: 451px; top: 45px; width: 350px; height: 45px;
    background: var(--green); border-radius: 3px; color: var(--white);
    font-family: "Mountains of Christmas", cursive; font-weight: 700; font-size: 40px;
    text-align: center; line-height: 45px; letter-spacing: 1px;
  }
  .testimonials {
    position: absolute; left: 451px; top: 100px; width: 360px;
    color: var(--ink); font-size: 12.5px; line-height: 21px;
  }
  .testimonials .author { font-weight: 700; margin-top: 19px; }
  .testimonials .gap { height: 21px; }

  .divider { position: absolute; left: 451px; top: 262px; width: 300px; height: 4px; }
  .pen-doodle {
    position: absolute; left: 740px; top: 225px; width: 48px; height: 44px;
    background: linear-gradient(135deg, rgba(120,120,120,.35), rgba(120,120,120,.1)); border-radius: 6px;
  }

  .bottom-band { position: absolute; left: 425px; top: 574px; width: 418px; height: 23px; background: var(--purple-dark); }
</style>
</head>
<body>
  <main class="flyer">
    <div class="kids-photo" role="img" aria-label="Photo of two young children standing back to back, each reading a book"></div>
    <div class="cap-doodle" role="img" aria-label="Sketch of a graduation cap"></div>
    <div class="bulb-doodle" role="img" aria-label="Sketch of a light bulb"></div>

    <div class="bottom-band"></div>

    <svg class="contact-panel" viewBox="0 0 843 597" aria-hidden="true">
      <circle cx="145" cy="613" r="305" fill="var(--purple-dark)"/>
      <circle cx="145" cy="613" r="295" fill="var(--purple)"/>
    </svg>

    <section class="contact">
      <h2>Contact Us</h2>
      <p>18 Wattle Lane, Banksia Grove, Western Australia 6031</p>
      <p>Phone : (08) 9400 2187</p>
      <p>Email : enquiries@tiny-sprouts.com.au</p>
      <p>website: www.tiny-sprouts.com.au</p>
      <p>Open Monday - Friday 6:00am - 6:00pm(except public holidays)</p>
      <div class="social">
        <p><span class="dot"></span>Like Us <strong>@tinysproutsOZ</strong></p>
        <p><span class="dot"></span>Follow our tweets <strong>@TinySproutsOZ</strong></p>
      </div>
    </section>

    <div class="reader-girl" role="img" aria-label="Cartoon of a little girl reading a book"></div>
    <h2 class="testimonials-title">Testimonials</h2>

    <section class="testimonials">
      <p>“My daughter has been attending the centre and has flourished in the environment. She is always excited to play with the other children and is very well looked after by the team.<br>I highly recommend Tiny Sprouts to anyone considering daycare options in the Banksia Grove area.”</p>
      <p class="author">Maren Holloway</p>
      <div class="gap"></div>
      <div class="gap"></div>
      <p>“My son Aravind has been with Tiny Sprouts for over a year and our experience has been one of a nurturing and caring environment. Aravind loves it each day and finds it really enjoyable in the environment of caring &amp; friendly staff &amp; his little buddies.</p>
      <div class="gap"></div>
      <p>He has grown up so much and developed in leaps and bounds since starting at your childcare which is very much evident to us. We are only in praise of your centre and to share the happiness, has made one of my colleague’s toddlers join too”. Thanks.</p>
      <p class="author">Rohan</p>
    </section>

    <svg class="divider" viewBox="0 0 300 4" aria-hidden="true">
      <line x1="0" y1="2" x2="300" y2="2" stroke="#666" stroke-width="1.2" stroke-dasharray="4 3"/>
    </svg>
    <div class="pen-doodle" role="img" aria-label="Sketch of a fountain pen"></div>
  </main>
</body>
</html>
```